Colorful Live Music Concert Poster for Tin Harbor

Looking for a portrait oriented "poster" promoting the band's upcoming show at Marlow Lounge on Sunday, 3/22 at 8 pm, and social version (square format for Instagram). <br/><br/>Copy:<br/>Tin Harbor<br/>with The Pale Wires<br/><br/>Marlow Lounge <br/>Sunday, March 22<br/>8 pm<br/><br/>Poster must be consistent with band's overall branding seen on www.tinharborband.example and it's Tunevault page at https://music.example.com/artist/7QxRtaWpLeNmVcz2Ks9DuB?si=381fkTsYpWmaGHeLoRqdXC <br/><br/>BUT, we wouldn't mind taking in a slightly updated direction. A good example is the cover for our recent single Glad Today, which is consistent in theme and color palette while updating the design and color at the same time. <br/><br/>The attached files include some band logo art as well as examples of posters done for prior shows. <br/><br/>The posters need not include photos of the band, but if you are so inclined, we've uploaded some selects as well.<br/><br/>Thank you. <br/><br/>Wendell<br/>Tin Harbor

```html
<!DOCTYPE html>
<html lang="en">
<head>
<meta charset="utf-8">
<title>Tin Harbor – Marlow Lounge Poster Samples</title>
<link rel="stylesheet" href="https://fonts.googleapis.com/css2?family=Montserrat:wght@300;400;700;800&display=swap">
<style>
  :root {
    --board: #363636;
    --teal: #17a7ad;
    --yellow: #fbb11a;
    --navy: #1d2b5a;
    --white: #ffffff;
    --label: #e8e8e8;
  }
  * { box-sizing: border-box; margin: 0; padding: 0; }
  html, body { width: 1200px; height: 664px; overflow: hidden; background: var(--board); }
  body { font-family: "Montserrat", sans-serif; position: relative; }

  .poster { position: absolute; top: 61px; width: 344px; height: 531px; overflow: hidden; }
  .poster--one { left: 46px; background: var(--teal); }
  .poster--two { left: 428px; background: var(--yellow); }
  .poster--three { left: 810px; background: var(--teal); }

  .sample-label { position: absolute; top: 602px; font-size: 12px; font-weight: 400; color: var(--label); letter-spacing: 0.5px; }

  /* shared pieces */
  .badge { position: absolute; border-radius: 50%; display: flex; align-items: center; justify-content: center; }
  .badge__ring { position: absolute; inset: 0; border-radius: 50%; border: 1px solid var(--yellow); }
  .badge__fill { position: absolute; border-radius: 50%; background: var(--yellow); }
  .badge__name { position: relative; text-align: center; font-weight: 800; color: var(--navy); line-height: 0.95; text-transform: uppercase; }

  .rule { position: absolute; height: 1px; background: var(--white); }

  .date { position: absolute; color: var(--white); text-transform: uppercase; }
  .date__day { font-size: 22px; font-weight: 400; line-height: 1; }
  .date__month { font-size: 31px; font-weight: 800; line-height: 1.05; letter-spacing: -0.5px; }
  .date__doors { font-size: 16px; font-weight: 400; line-height: 1.1; }

  .socials { position: absolute; display: flex; gap: 9px; color: var(--navy); font-size: 6px; align-items: center; }
  .socials__item { display: flex; align-items: center; gap: 3px; }
  .socials__dot { width: 8px; height: 8px; border-radius: 50%; background: var(--yellow); }

  /* poster one */
  .brick-orb { position: absolute; left: 38px; top: 25px; width: 270px; height: 270px; border-radius: 50%;
    background: radial-gradient(circle at 48% 53%, var(--yellow) 0%, var(--yellow) 27%, var(--navy) 38%, var(--navy) 100%); }
  .headline-band { position: absolute; left: 0; width: 100%; text-align: center; color: var(--navy); text-transform: uppercase; }
  .poster--one .band-name { top: 314px; font-size: 31px; font-weight: 400; letter-spacing: 6px; }
  .poster--one .support-act { top: 350px; font-size: 19px; font-weight: 800; letter-spacing: 0.5px; }

  /* poster two */
  .poster--two .band-name { position: absolute; left: 0; width: 100%; text-align: center; color: var(--navy); font-weight: 400; text-transform: uppercase; line-height: 1; }
  .poster--two .band-name__first { top: 28px; font-size: 60px; letter-spacing: 14px; }
  .poster--two .band-name__second { top: 100px; font-size: 62px; letter-spacing: 6px; }
  .support-bar { position: absolute; left: 0; top: 184px; width: 100%; height: 45px; background: var(--navy); color: var(--white);
    display: flex; align-items: center; justify-content: center; font-size: 28px; font-weight: 800; text-transform: uppercase; }
  .poster--two .badge__ring { border-color: var(--white); }
  .poster--two .badge__fill { background: var(--white); }
  .poster--two .date { left: 0; width: 100%; text-align: center; }
  .poster--two .date__line { font-size: 27px; font-weight: 800; line-height: 1; letter-spacing: -0.3px; }
  .poster--two .date__doors { font-size: 20px; font-weight: 300; margin-top: 5px; }
  .footer-bar { position: absolute; left: 0; top: 492px; width: 100%; height: 39px; background: var(--navy);
    display: flex; align-items: center; justify-content: center; }
  .footer-bar .socials { position: static; color: var(--white); font-size: 9px; gap: 10px; }
  .footer-bar .socials__dot { width: 12px; height: 12px; }

  /* poster three */
  .brick-haze { position: absolute; left: 214px; top: 125px; width: 200px; height: 275px; border-radius: 50% 0 0 50%;
    background: radial-gradient(ellipse at 70% 50%, rgba(15, 150, 160, 0.9) 0%, rgba(15, 150, 160, 0.35) 60%, rgba(23, 167, 173, 0) 100%); }
  .vertical-name { position: absolute; writing-mode: vertical-rl; transform: rotate(180deg); color: var(--navy);
    font-weight: 400; text-transform: uppercase; line-height: 1; white-space: nowrap; }
  .vertical-name--first { left: 52px; top: 150px; height: 205px; font-size: 74px; letter-spacing: 16px; text-align: left; }
  .vertical-name--second { left: 141px; top: 28px; height: 364px; font-size: 74px; letter-spacing: 6px; }
</style>
</head>
<body>

  <!-- Poster one -->
  <section class="poster poster--one" aria-label="Poster sample one">
    <div class="brick-orb" role="img" aria-label="Round brick wall illustration with a glowing yellow window at its centre"></div>
    <h1 class="headline-band band-name">Tin Harbor</h1>
    <p class="headline-band support-act">The Pale Wires</p>

    <div class="badge" style="left:17px;top:396px;width:112px;height:112px;">
      <span class="badge__ring"></span>
      <span class="badge__fill" style="inset:5px;"></span>
      <span class="badge__name" style="font-size:17px;">Marlow<br>Lounge</span>
    </div>

    <div class="rule" style="left:138px;top:412px;width:190px;"></div>
    <div class="date" style="left:138px;top:418px;">
      <div class="date__day">Sunday</div>
      <div class="date__month">March 22</div>
      <div class="date__doors">Door at 8 pm</div>
    </div>
    <div class="rule" style="left:138px;top:491px;width:190px;"></div>

    <div class="socials" style="left:140px;top:500px;">
      <span class="socials__item"><span class="socials__dot"></span>@tinharborband</span>
      <span class="socials__item"><span class="socials__dot"></span>@tinharborband</span>
      <span class="socials__item"><span class="socials__dot"></span>/tinharborband</span>
    </div>
  </section>
  <p class="sample-label" style="left:46px;">SAMPLE 1</p>

  <!-- Poster two -->
  <section class="poster poster--two" aria-label="Poster sample two">
    <h2 class="band-name band-name__first">Tin</h2>
    <h2 class="band-name band-name__second">Harbor</h2>
    <div class="support-bar">The Pale Wires</div>

    <div class="badge" style="left:97px;top:250px;width:150px;height:150px;">
      <span class="badge__ring"></span>
      <span class="badge__fill" style="inset:7px;"></span>
      <span class="badge__name" style="font-size:24px;">Marlow<br>Lounge</span>
    </div>

    <div class="rule" style="left:30px;top:412px;width:284px;"></div>
    <div class="date" style="top:418px;">
      <div class="date__line">Sunday, March 22</div>
      <div class="date__doors">Door at 8 pm</div>
    </div>
    <div class="rule" style="left:30px;top:474px;width:284px;"></div>

    <div class="footer-bar">
      <div class="socials">
        <span class="socials__item"><span class="socials__dot"></span>@tinharborband</span>
        <span class="socials__item"><span class="socials__dot"></span>@tinharborband</span>
        <span class="socials__item"><span class="socials__dot"></span>/tinharborband</span>
      </div>
    </div>
  </section>
  <p class="sample-label" style="left:426px;">SAMPLE 2</p>

  <!-- Poster three -->
  <section class="poster poster--three" aria-label="Poster sample three">
    <div class="brick-haze" role="img" aria-label="Faint brick wall texture fading in from the right edge"></div>
    <h2 class="vertical-name vertical-name--first">Tin</h2>
    <h2 class="vertical-name vertical-name--second">Harbor</h2>

    <div class="badge" style="left:222px;top:27px;width:108px;height:108px;">
      <span class="badge__ring"></span>
      <span class="badge__fill" style="inset:5px;"></span>
      <span class="badge__name" style="font-size:16px;">The Pale<br>Wires</span>
    </div>

    <div class="badge" style="left:17px;top:396px;width:112px;height:112px;">
      <span class="badge__ring"></span>
      <span class="badge__fill" style="inset:5px;"></span>
      <span class="badge__name" style="font-size:17px;">Marlow<br>Lounge</span>
    </div>

    <div class="rule" style="left:138px;top:412px;width:190px;"></div>
    <div class="date" style="left:138px;top:418px;">
      <div class="date__day">Sunday</div>
      <div class="date__month">March 22</div>
      <div class="date__doors">Door at 8 pm</div>
    </div>
    <div class="rule" style="left:138px;top:491px;width:190px;"></div>

    <div class="socials" style="left:140px;top:500px;">
      <span class="socials__item"><span class="socials__dot"></span>@tinharborband</span>
      <span class="socials__item"><span class="socials__dot"></span>@tinharborband</span>
      <span class="socials__item"><span class="socials__dot"></span>/tinharborband</span>
    </div>
  </section>
  <p class="sample-label" style="left:809px;">SAMPLE 3</p>

</body>
</html>
```